Brindlecove Business Card

Looking for a new business Card layout for our company, brindlecove.

Logo Text

Standard Business Card , Name, email, phone, website. www.brindlecove-example.com

```html
<!DOCTYPE html>
<html lang="en">
<head>
<meta charset="utf-8">
<title>Brindlecove Business Card</title>
<link rel="stylesheet" href="https://fonts.googleapis.com/css2?family=Montserrat:wght@500;600;800&family=Open+Sans:wght@400&display=swap">
<style>
  :root {
    --stage: #2a3550;
    --card-white: #f7f7f5;
    --brand-blue: #3aa5d3;
    --ink-white: #ffffff;
    --shadow: rgba(8, 12, 28, 0.45);
  }
  * { margin: 0; padding: 0; box-sizing: border-box; }
  html, body { width: 1200px; height: 1016px; overflow: hidden; }
  body {
    background: var(--stage);
    font-family: "Montserrat", sans-serif;
    position: relative;
  }
  .card {
    position: absolute;
    left: 250px;
    width: 700px;
    height: 400px;
    box-shadow: 0 18px 40px var(--shadow);
  }
  .card--front { top: 64px; background: var(--card-white); }
  .card--back { top: 552px; background: var(--brand-blue); color: var(--ink-white); }

  .wordmark {
    position: absolute;
    inset: 0;
    display: flex;
    align-items: center;
    justify-content: center;
    gap: 16px;
  }
  .wordmark__dot {
    width: 30px; height: 30px;
    border-radius: 50%;
    background: var(--brand-blue);
  }
  .wordmark__name {
    font-weight: 800;
    font-size: 50px;
    letter-spacing: -1px;
    text-transform: uppercase;
    color: var(--brand-blue);
  }

  .holder {
    position: absolute;
    left: 60px;
    top: 150px;
  }
  .holder__name-row { display: flex; align-items: center; gap: 14px; }
  .holder__name {
    font-weight: 600;
    font-size: 38px;
    letter-spacing: 2px;
    text-transform: uppercase;
  }
  .holder__rule {
    width: 150px;
    height: 2px;
    background: var(--ink-white);
  }
  .holder__title {
    margin-top: 4px;
    font-weight: 600;
    font-size: 20px;
    letter-spacing: 3px;
    text-transform: uppercase;
  }

  .contact {
    position: absolute;
    left: 64px;
    top: 262px;
    list-style: none;
    font-family: "Open Sans", sans-serif;
    font-size: 16px;
  }
  .contact__item {
    display: flex;
    align-items: center;
    gap: 10px;
    height: 27px;
  }
  .contact__icon { width: 18px; height: 18px; flex: none; }
</style>
</head>
<body>
  <section class="card card--front" aria-label="Card front">
    <div class="wordmark">
      <span class="wordmark__dot"></span>
      <span class="wordmark__name">Brindlecove</span>
    </div>
  </section>

  <section class="card card--back" aria-label="Card back">
    <div class="holder">
      <div class="holder__name-row">
        <h1 class="holder__name">Marta Keller</h1>
        <span class="holder__rule"></span>
      </div>
      <p class="holder__title">Superviser</p>
    </div>

    <ul class="contact">
      <li class="contact__item">
        <svg class="contact__icon" viewBox="0 0 18 18" aria-hidden="true">
          <circle cx="9" cy="9" r="9" fill="#fff"/>
          <path d="M6 4.5l1.6 0 .8 2.2-1 .8a6 6 0 0 0 2.8 2.8l.8-1 2.2.8v1.6c0 .6-.5 1-1.1 1A7.5 7.5 0 0 1 5 5.6c0-.6.4-1.1 1-1.1z" fill="#3aa5d3"/>
        </svg>
        <span>1-555-014-2270</span>
      </li>
      <li class="contact__item">
        <svg class="contact__icon" viewBox="0 0 18 18" aria-hidden="true">
          <circle cx="9" cy="9" r="9" fill="#fff"/>
          <rect x="4.5" y="5.8" width="9" height="6.4" rx="0.8" fill="#3aa5d3"/>
          <path d="M4.8 6.2L9 9.4l4.2-3.2" stroke="#fff" stroke-width="0.9" fill="none"/>
        </svg>
        <span>info@brindlecove-example.com</span>
      </li>
      <li class="contact__item">
        <svg class="contact__icon" viewBox="0 0 18 18" aria-hidden="true">
          <circle cx="9" cy="9" r="9" fill="#fff"/>
          <circle cx="9" cy="9" r="4.6" fill="none" stroke="#3aa5d3" stroke-width="1.1"/>
          <path d="M4.4 9h9.2M9 4.4c-2.2 2.6-2.2 6.6 0 9.2M9 4.4c2.2 2.6 2.2 6.6 0 9.2" stroke="#3aa5d3" stroke-width="1" fill="none"/>
        </svg>
        <span>www.brindlecove-example.com</span>
      </li>
      <li class="contact__item">
        <svg class="contact__icon" viewBox="0 0 18 18" aria-hidden="true">
          <circle cx="9" cy="9" r="9" fill="#fff"/>
          <path d="M9 4a3.3 3.3 0 0 1 3.3 3.3C12.3 10 9 14 9 14S5.7 10 5.7 7.3A3.3 3.3 0 0 1 9 4z" fill="#3aa5d3"/>
          <circle cx="9" cy="7.3" r="1.2" fill="#fff"/>
        </svg>
        <span>48 Alder Lane, GRMNY</span>
      </li>
    </ul>
  </section>
</body>
</html>
```